Post storm repair flyer

looking for an eye catching 6x9 postcard to send out to single family home owners advertising a "Post Storm Repair Special" explaining that after the recent hurricanes its very important to have your roof checked and any repairs fixed right away before they become a bigger more costly problem and that even though your home wasn't directly hit by the storm the high wind gust could've cause unseen damage.
offer $200 off any repair *some rules may apply
Crest Roofing
877.512.TOPS
www.CrestRoofingco.example

```html
<!DOCTYPE html>
<html lang="en">
<head>
<meta charset="utf-8">
<title>Crest Roofing – Post Storm Repair Special Postcard</title>
<link href="https://fonts.googleapis.com/css2?family=Bebas+Neue&family=Jost:wght@300;400;600&family=Montserrat:wght@500;600;700&display=swap" rel="stylesheet">
<style>
  :root {
    --backdrop: #fbb94f;
    --paper: #ffffff;
    --ink: #1b1b1b;
    --panel: #1a1a1a;
    --gold: #fbbd14;
    --rule-grey: #a7a7a7;
    --faint: #e4e4e4;
  }
  * { margin: 0; padding: 0; box-sizing: border-box; }
  html, body { width: 922px; height: 1200px; overflow: hidden; }
  body { background: var(--backdrop); position: relative; font-family: "Montserrat", sans-serif; }

  .card {
    position: absolute; left: 71px; width: 780px; height: 520px;
    background: var(--paper); overflow: hidden;
    box-shadow: 0 8px 18px rgba(0,0,0,.18);
  }
  .card--front { top: 70px; }
  .card--back { top: 610px; }
  .card svg.shapes { position: absolute; inset: 0; }
  .abs { position: absolute; }

  .brand-name { font-family: "Jost", sans-serif; font-weight: 600; letter-spacing: .3px; white-space: nowrap; }
  .front-brand { left: 32px; top: 52px; font-size: 31px; line-height: 1; color: var(--ink); display: flex; align-items: center; gap: 14px; }
  .front-brand .mark-square { width: 26px; height: 26px; background: var(--gold); }

  .headline { font-family: "Bebas Neue", sans-serif; font-weight: 400; line-height: 54px; left: 32px; top: 136px; font-size: 64px; white-space: nowrap; }
  .headline .accent { color: var(--gold); display: block; }
  .headline .main { color: #fff; display: block; }

  .thumb { top: 258px; width: 121px; height: 77px; }
  .gold-rule { height: 2px; background: var(--gold); }
  .front-copy { left: 32px; top: 355px; width: 396px; font-size: 11.8px; font-weight: 500; line-height: 17px; color: #fff; text-align: justify; }
  .offer { left: 32px; top: 409px; font-size: 12px; font-weight: 700; color: var(--gold); white-space: nowrap; }
  .offer small { font-size: 9.5px; font-weight: 500; color: #fff; margin-left: 6px; }

  .contact-name { font-family: "Jost", sans-serif; font-weight: 400; white-space: nowrap; }
  .phone { font-family: "Bebas Neue", sans-serif; color: var(--gold); letter-spacing: .5px; white-space: nowrap; }
  .web { font-family: "Jost", sans-serif; font-weight: 300; white-space: nowrap; }

  .front-contact-name { left: 33px; top: 455px; font-size: 22px; color: var(--ink); line-height: 1; }
  .front-phone { left: 33px; top: 476px; font-size: 34px; line-height: 1; }
  .front-web { right: 24px; top: 478px; font-size: 19px; color: var(--ink); }

  .back-brand { left: 28px; top: 100px; font-size: 27px; color: #fff; }
  .back-copy { left: 28px; top: 182px; width: 330px; font-size: 23.5px; font-weight: 500; line-height: 29px; color: #fff; }
  .back-contact-name { left: 28px; top: 412px; font-size: 23px; color: #fff; line-height: 1; }
  .back-phone { left: 28px; top: 432px; font-size: 33px; line-height: 1; }
  .back-web { left: 28px; top: 462px; font-size: 19px; color: #fff; }

  .stamp-box { left: 630px; top: 38px; width: 122px; height: 121px; border: 2px solid var(--rule-grey); }
  .address-line { left: 535px; width: 220px; height: 2px; background: var(--rule-grey); }
  .faint-brand { right: 28px; bottom: 30px; font-size: 16px; color: var(--faint); }
</style>
</head>
<body>

<section class="card card--front">
  <svg class="shapes" width="780" height="520" viewBox="0 0 780 520">
    <defs>
      <linearGradient id="roofPhoto" x1="0" y1="0" x2="0" y2="1">
        <stop offset="0" stop-color="#dfe6ec"/>
        <stop offset=".45" stop-color="#9aa6b0"/>
        <stop offset="1" stop-color="#545a60"/>
      </linearGradient>
    </defs>
    <path role="img" aria-label="Photo of roofers in hard hats hammering shingles on a roof"
          d="M362 94 H780 V455 H362 Q313 455 313 406 V143 Q313 94 362 94 Z" fill="url(#roofPhoto)"/>
    <path d="M0 114 H420 Q450 114 468 140 L540 245 Q560 274 540 303 L468 409 Q450 435 420 435 H0 Z" fill="var(--panel)"/>
  </svg>

  <div class="abs front-brand"><span class="mark-square"></span><span class="brand-name">CREST ROOFING</span></div>

  <h1 class="abs headline"><span class="accent">Post Storm</span><span class="main">Repair Special</span></h1>

  <div class="abs thumb" role="img" aria-label="Storm-damaged shingles with missing patches" style="left:32px;background:linear-gradient(135deg,#7d8088,#b3b6ba,#5f636a)"></div>
  <div class="abs thumb" role="img" aria-label="Roof covered with a blue tarp among trees" style="left:159px;background:linear-gradient(135deg,#4f7a3c,#3b8fd6,#7bb3e6)"></div>
  <div class="abs thumb" role="img" aria-label="Repaired roof gable with white trim" style="left:286px;background:linear-gradient(135deg,#4a4d52,#c9c2b6,#8f8a82)"></div>

  <div class="abs gold-rule" style="left:32px;top:346px;width:199px"></div>

  <p class="abs front-copy">After the recent hurricanes, it's very important to have your roof checked and any repairs fixed right away before they become a bigger, more costly problem.</p>

  <p class="abs offer">$200 OFF ANY REPAIR<small>*some rules may apply</small></p>

  <div class="abs contact-name front-contact-name">CREST ROOFING</div>
  <div class="abs phone front-phone">877.512.TOPS</div>
  <div class="abs web front-web">www.CrestRoofingco.example</div>
</section>

<section class="card card--back">
  <svg class="shapes" width="780" height="520" viewBox="0 0 780 520">
    <defs>
      <linearGradient id="darkPhoto" x1="0" y1="0" x2="1" y2="1">
        <stop offset="0" stop-color="#151515"/>
        <stop offset=".6" stop-color="#262422"/>
        <stop offset="1" stop-color="#111"/>
      </linearGradient>
    </defs>
    <path role="img" aria-label="Darkened photo of roofers working on shingles"
          d="M0 0 H280 Q314 0 334 30 L434 225 Q449 263 434 300 L334 475 Q307 520 259 520 H0 Z" fill="url(#darkPhoto)"/>
  </svg>

  <div class="abs brand-name back-brand">CREST ROOFING</div>

  <p class="abs back-copy">Even though your home wasn't directly hit by the storm, the highest wind gust could've caused unseen damage.</p>

  <div class="abs gold-rule" style="left:28px;top:337px;width:217px"></div>

  <div class="abs contact-name back-contact-name">CREST ROOFING</div>
  <div class="abs phone back-phone">877.512.TOPS</div>
  <div class="abs web back-web">www.CrestRoofingco.example</div>

  <div class="abs stamp-box"></div>
  <div class="abs address-line" style="top:208px"></div>
  <div class="abs address-line" style="top:255px"></div>
  <div class="abs address-line" style="top:302px"></div>

  <div class="abs brand-name faint-brand">CREST ROOFING</div>
</section>

</body>
</html>
```